Rack card for a integrative medical practice

Need an eye-catching rack card with our logo with content as provided. We have a membership based holistic medical practice which incorporates western and holistic medicine. We would like to focus on wellness and healthy lifestyle. See uploaded files for what is included in the membership. Would like 2 page rack card color on both sides. Logo must be on the front.

Target Market(s)

People looking for alternative medicine, healthy lifestyle.

Industry/Entity Type

Health and Wellness

Colors
00AB8E
00BBA5
67D7C9
C6EFE9
E9F9F6

Requirements
Must have
• Must spark interest at first sight. Clear message.
Nice to have
• Warm, bright and positive vibe. Organic, neutral and earthy colors.
Should not have
• Traditional medical practice vibe (cold, formal, industrial). No PINK except the logo.

```html
<!DOCTYPE html>
<html lang="en">
<head>
<meta charset="utf-8">
<title>Amaryn Health &amp; Wellness – Rack Card</title>
<link href="https://fonts.googleapis.com/css2?family=Alice&family=Cinzel:wght@500;600&family=Josefin+Sans:wght@400&family=Montserrat:wght@400;700&display=swap" rel="stylesheet">
<style>
  :root {
    --backdrop: #bdbdbd;
    --paper: #ffffff;
    --teal-deep: #00AB8E;
    --teal: #00BBA5;
    --teal-soft: #67D7C9;
    --mint: #C6EFE9;
    --mint-pale: #E9F9F6;
    --forest: #0f3b2e;
    --ink: #3b3b3b;
    --photo-warm: #c98a6a;
    --photo-cool: #6c7fa8;
  }
  * { box-sizing: border-box; margin: 0; padding: 0; }
  html, body { width: 916px; height: 1200px; overflow: hidden; }
  body { background: var(--backdrop); position: relative; font-family: "Montserrat", sans-serif; }

  .rack-card {
    position: absolute; top: 127px; width: 420px; height: 945px;
    background: var(--paper); box-shadow: 0 2px 6px rgba(0,0,0,.18); overflow: hidden;
  }
  .rack-card--back { left: 25px; }
  .rack-card--front { left: 471px; }

  .brand { position: absolute; left: 0; right: 0; text-align: center; color: var(--forest); font-family: "Cinzel", serif; font-weight: 500; }
  .brand__dot { display: block; margin: 0 auto 14px; border-radius: 50%; background: var(--teal); }
  .brand__name { display: block; letter-spacing: .14em; line-height: 1; }
  .brand__sub { display: block; letter-spacing: .35em; margin-top: 6px; }

  .rack-card--back .brand { top: 40px; }
  .rack-card--back .brand__dot { width: 58px; height: 58px; }
  .rack-card--back .brand__name { font-size: 42px; }
  .rack-card--back .brand__sub { font-size: 11px; }

  .rack-card--front .brand { top: 44px; }
  .rack-card--front .brand__dot { width: 72px; height: 72px; }
  .rack-card--front .brand__name { font-size: 50px; }
  .rack-card--front .brand__sub { font-size: 12px; }

  .ribbon { position: absolute; left: 0; }
  .ribbon svg { position: absolute; inset: 0; width: 100%; height: 100%; }
  .ribbon__text { position: relative; color: var(--paper); font-weight: normal; }

  .ribbon--membership { top: 203px; width: 390px; height: 120px; }
  .ribbon--membership .ribbon__text {
    font-family: "Cinzel", serif; font-weight: 600; font-size: 28.5px; line-height: 31px;
    padding: 28px 30px 0 22px; text-align: left;
  }

  .benefits { position: absolute; top: 345px; left: 34px; right: 28px; list-style: none; }
  .benefits li {
    position: relative; padding-left: 18px; margin-bottom: 17px;
    font-size: 17.5px; line-height: 21px; color: var(--ink);
  }
  .benefits li::before {
    content: ""; position: absolute; left: 0; top: 7px; width: 5px; height: 5px;
    border: 1.5px solid var(--teal-deep); border-radius: 50%;
  }

  .address { position: absolute; top: 828px; left: 0; right: 0; display: flex; justify-content: center; align-items: center; gap: 6px; color: var(--teal-deep); font-weight: 700; font-size: 14px; line-height: 19px; }
  .contact { position: absolute; top: 895px; left: 32px; right: 20px; display: flex; justify-content: space-between; color: var(--teal-deep); font-size: 12.5px; }
  .contact span, .address span.icon { display: flex; align-items: center; gap: 6px; }
  .icon svg { display: block; }

  .photo { position: absolute; top: 247px; left: 0; width: 420px; height: 272px;
    background: linear-gradient(135deg, var(--photo-warm) 0%, #a07a80 45%, var(--photo-cool) 100%); }

  .ribbon--title { top: 544px; width: 362px; height: 92px; }
  .ribbon--title .ribbon__text {
    font-family: "Alice", serif; font-size: 33px; line-height: 31px; padding: 14px 40px 0 10px; text-align: center;
  }

  .tagline { position: absolute; top: 679px; left: 40px; right: 40px; text-align: center;
    font-family: "Josefin Sans", sans-serif; font-size: 23.5px; line-height: 28px; color: var(--ink); text-transform: uppercase; }

  .site-band { position: absolute; bottom: 0; left: 0; right: 0; height: 82px; background: var(--teal-deep);
    color: var(--paper); font-family: "Alice", serif; font-size: 19px; display: flex; align-items: center; justify-content: center; }
</style>
</head>
<body>

<section class="rack-card rack-card--back">
  <div class="brand">
    <span class="brand__dot"></span>
    <span class="brand__name">AMARYN</span>
    <span class="brand__sub">HEALTH &amp; WELLNESS</span>
  </div>

  <div class="ribbon ribbon--membership">
    <svg viewBox="0 0 390 120" preserveAspectRatio="none"><polygon points="0,0 390,0 362,60 390,120 0,120" fill="var(--teal-deep)"/></svg>
    <h2 class="ribbon__text">WHAT'S INCLUDED IN<br>YOUR MEMBERSHIP :</h2>
  </div>

  <ul class="benefits">
    <li>Unlimited office visits with no copay</li>
    <li>Direct communication with your doctor</li>
    <li>Discounted labs, imaging and medications</li>
    <li>Free initial acupuncture session ($250 value).</li>
    <li>2 Vitalis testings per year ($100 value)</li>
    <li>Discounts for supplements and health products in the clinic</li>
    <li>Discounts for iv vitamin infusion therapy</li>
    <li>Personalized nutrition plan after advanced testing such as gut microbiome, hormonal, metabolismtest, etc.</li>
  </ul>

  <div class="address">
    <span class="icon"><svg width="22" height="22" viewBox="0 0 22 22"><circle cx="11" cy="11" r="10" fill="none" stroke="var(--teal-deep)" stroke-width="1.3"/><path d="M11 16c-3-3.5-4-5-4-6.5a4 4 0 0 1 8 0c0 1.5-1 3-4 6.5z" fill="none" stroke="var(--teal-deep)" stroke-width="1.3"/><circle cx="11" cy="9.5" r="1.3" fill="var(--teal-deep)"/></svg></span>
    <div>1420 W Elm Ave., STE 2B<br>Brookfield, IN 46000</div>
  </div>

  <div class="contact">
    <span><svg width="20" height="20" viewBox="0 0 20 20"><circle cx="10" cy="10" r="9" fill="none" stroke="var(--teal-deep)" stroke-width="1.2"/><rect x="7" y="5" width="6" height="10" rx="1.2" fill="none" stroke="var(--teal-deep)" stroke-width="1.2"/></svg>(555) 210-4477</span>
    <span><svg width="20" height="20" viewBox="0 0 20 20"><circle cx="10" cy="10" r="9" fill="none" stroke="var(--teal-deep)" stroke-width="1.2"/><circle cx="10" cy="10" r="5" fill="none" stroke="var(--teal-deep)" stroke-width="1"/><path d="M5 10h10M10 5c-2 3-2 7 0 10M10 5c2 3 2 7 0 10" fill="none" stroke="var(--teal-deep)" stroke-width="1"/></svg>www.amaryntotalhealth.com</span>
  </div>
</section>

<section class="rack-card rack-card--front">
  <div class="brand">
    <span class="brand__dot"></span>
    <span class="brand__name">AMARYN</span>
    <span class="brand__sub">HEALTH &amp; WELLNESS</span>
  </div>

  <div class="photo" role="img" aria-label="Photo of a group yoga class stretching on mats"></div>

  <div class="ribbon ribbon--title">
    <svg viewBox="0 0 362 92" preserveAspectRatio="none"><polygon points="0,0 362,0 336,46 362,92 0,92" fill="var(--teal-deep)"/></svg>
    <h1 class="ribbon__text">Amaryn Health &amp;<br>Wellness</h1>
  </div>

  <p class="tagline">A direct primary care practice focused on a more holistic and personal approach to medicine.</p>

  <div class="site-band">www.amaryntotalhealth.com</div>
</section>

</body>
</html>
```